4 Banners Required for Credit Card Comparison website

Project:

Creation of online advertising banners for use on Quorvel AdLink network and for display advertising on PalHaven.com

Headline to appear on all banners:
Save up to $1,000 or more in interest with a Balance Transfer Credit Card. Compare the offers on (logo)

Formats
- 728 x 90
- 468 x 60
- 300 x 250
- 160 x 600

Background:

Card Match Scout (http://www.cardmatchscout.example.au) is a credit card comparison service that compares the best credit cards in the Australian market. It helps consumers to find the right credit card for them. CMS want to attract more people to our site to compare and apply for credit cards online. The primary focus is for customers to compare the card offers on our comparison tables and apply online as opposed to going to a bank, calling or going to the bank site directly.

Desired Outcomes:
1. Viewers click on the banner and go through to Card Match Scout
2. New people click on the banner ad and go to our website, compare the cards and apply online
3. Get people to subscribe to our credit card email alert service

Note: Would prefer to have banners ASAP (sooner than 5 days if possible). Designers who act on it quickly, and supply great designs will most likely be awarded the winner
Updates

Thanks for the great work so far - we are really liking the submissions :)

Question - does anyone that has submitted a design so far have the ability to create flash banners? We are also considering our options as we have heard that flash banners are sometimes more effective

Cheers

Tobias

Target Market(s)

- Australian Credit Card users
- 18+ male and female
- Savvy people wanting a better deal on their credit card

Industry/Entity Type

Credit Card

Requirements
Must have
• - Need to quickly explain the simple concept that the website provides.
- Don’t want to use metaphors, prefer to use screenshots of the comparison table
- Simple 1 line headline with an easy call to action
Nice to have
• - Suggest different headline to the one we''ve proposed
Should not have
• The design should not use old-style, serif fonts like Times New Roman. Do not include illustrations of money bags or gold bullions or tacky design elements you see on low quality money-related websites.

```html
<!DOCTYPE html>
<html lang="en">
<head>
<meta charset="utf-8">
<title>Card Match Scout — Balance Transfer Banners</title>
<link rel="stylesheet" href="https://fonts.googleapis.com/css2?family=Poppins:wght@400;500;700;800&display=swap">
<style>
  :root {
    --blue: #2d5cab;
    --blue-light: #4a7dcb;
    --blue-edge: #2a56a3;
    --white: #ffffff;
    --green-top: #7fcf6a;
    --green-bottom: #2f9a36;
    --brand-blue: #2a5aa9;
    --ink: #1c1c1c;
    --page: #ffffff;
  }
  * { box-sizing: border-box; margin: 0; padding: 0; }
  html, body { width: 1109px; height: 1200px; overflow: hidden; background: var(--page); }
  body { position: relative; font-family: "Poppins", Arial, sans-serif; }

  .banner {
    position: absolute;
    background: var(--blue);
    border: 3px solid var(--blue-edge);
    border-radius: 12px;
    overflow: hidden;
    color: var(--white);
  }
  .sheen { position: absolute; inset: 0; width: 100%; height: 100%; }

  .white-panel { position: absolute; background: var(--white); }

  .headline {
    position: absolute;
    font-weight: 800;
    text-transform: uppercase;
    text-align: center;
    letter-spacing: 0.5px;
    line-height: 1;
    white-space: nowrap;
  }
  .subline { position: absolute; font-weight: 400; text-align: center; white-space: nowrap; }
  .subline em { font-style: italic; font-weight: 700; }

  .cta {
    position: absolute;
    border-radius: 999px;
    background: linear-gradient(var(--green-top), var(--green-bottom));
    color: var(--white);
    display: flex; align-items: center; justify-content: center;
    text-align: center;
    font-weight: 400;
    line-height: 1.05;
    white-space: nowrap;
    box-shadow: inset 0 1px 0 rgba(255,255,255,.5);
  }

  .brand-mark { position: absolute; background: var(--brand-blue); border-radius: 4px; }
  .brand-name { position: absolute; color: var(--brand-blue); font-weight: 700; white-space: nowrap; letter-spacing: -0.3px; line-height: 1.2; }
  .brand-tagline { position: absolute; color: var(--ink); font-weight: 400; white-space: nowrap; text-align: center; line-height: 1.3; }

  /* 160 x 600 skyscraper */
  .skyscraper { left: 160px; top: 6px; width: 234px; height: 885px; }
  .skyscraper .white-panel { left: 0; right: 0; top: 612px; bottom: 0; }
  .skyscraper .headline { left: 0; right: 0; top: 24px; font-size: 58px; line-height: 68px; }
  .skyscraper .subline { left: 0; right: 0; top: 444px; font-size: 30px; line-height: 41px; }
  .skyscraper .cta { left: 15px; top: 622px; width: 203px; height: 58px; font-size: 22px; white-space: normal; }
  .skyscraper .brand-mark { left: 85px; top: 705px; width: 62px; height: 62px; }
  .skyscraper .brand-name { left: 0; right: 0; top: 790px; text-align: center; font-size: 22px; }
  .skyscraper .brand-tagline { left: 0; right: 0; top: 826px; font-size: 16px; line-height: 20px; }

  /* 300 x 250 rectangle */
  .rectangle { left: 442px; top: 518px; width: 443px; height: 367px; }
  .rectangle .white-panel { left: 0; right: 0; top: 239px; bottom: 0; }
  .rectangle .headline { left: 0; right: 0; top: 8px; font-size: 56px; line-height: 66px; }
  .rectangle .subline { left: 0; right: 0; top: 206px; font-size: 18px; }
  .rectangle .cta { left: 90px; top: 251px; width: 285px; height: 34px; font-size: 22px; }
  .rectangle .brand-mark { left: 20px; top: 268px; width: 60px; height: 60px; }
  .rectangle .brand-name { left: 95px; top: 292px; font-size: 31px; line-height: 1; }
  .rectangle .brand-tagline { left: 95px; top: 326px; font-size: 19px; text-align: left; }

  /* 728 x 90 leaderboard */
  .leaderboard { left: 15px; top: 902px; width: 1077px; height: 129px; }
  .leaderboard .white-panel { left: 633px; right: 0; top: 0; bottom: 0; clip-path: polygon(59px 0, 100% 0, 100% 100%, 0 100%); }
  .leaderboard .headline { left: 16px; top: 16px; font-size: 64px; letter-spacing: 1.5px; text-align: left; }
  .leaderboard .subline { left: 16px; top: 86px; font-size: 21px; text-align: left; }
  .leaderboard .cta { left: 761px; top: 12px; width: 267px; height: 33px; font-size: 21px; }
  .leaderboard .brand-mark { left: 690px; top: 36px; width: 56px; height: 56px; }
  .leaderboard .brand-name { left: 767px; top: 54px; font-size: 31px; line-height: 1; }
  .leaderboard .brand-tagline { left: 769px; top: 88px; font-size: 18px; text-align: left; }

  /* 468 x 60 banner */
  .full-banner { left: 189px; top: 1056px; width: 691px; height: 86px; border-width: 2px; border-radius: 8px; }
  .full-banner .white-panel { left: 423px; right: 0; top: 0; bottom: 0; clip-path: polygon(40px 0, 100% 0, 100% 100%, 0 100%); }
  .full-banner .headline { left: 9px; top: 10px; font-size: 40px; letter-spacing: 0.8px; text-align: left; }
  .full-banner .subline { left: 9px; top: 56px; font-size: 13.5px; text-align: left; }
  .full-banner .cta { left: 483px; top: 7px; width: 181px; height: 23px; font-size: 14px; }
  .full-banner .brand-mark { left: 438px; top: 32px; width: 34px; height: 34px; }
  .full-banner .brand-name { left: 482px; top: 36px; font-size: 20px; line-height: 1; }
  .full-banner .brand-tagline { left: 484px; top: 59px; font-size: 11px; text-align: left; }
</style>
</head>
<body>

<section class="banner skyscraper" aria-label="160 by 600 banner">
  <svg class="sheen" viewBox="0 0 234 885" preserveAspectRatio="none" aria-hidden="true">
    <path d="M234 0 C180 160 110 330 20 612 L234 612 Z" fill="var(--blue-light)" opacity=".45"/>
  </svg>
  <div class="white-panel"></div>
  <h2 class="headline">Save<br>up<br>to<br>$1000<br>or<br>more</h2>
  <p class="subline">with a<br>Balance<br>Transfer<br>Credit Card</p>
  <a class="cta">Compare the<br>Offers</a>
  <span class="brand-mark"></span>
  <span class="brand-name">CardMatchScout</span>
  <span class="brand-tagline">Find the best<br>credit card for you</span>
</section>

<section class="banner rectangle" aria-label="300 by 250 banner">
  <svg class="sheen" viewBox="0 0 443 367" preserveAspectRatio="none" aria-hidden="true">
    <path d="M443 0 C360 70 260 150 120 239 L443 239 Z" fill="var(--blue-light)" opacity=".4"/>
  </svg>
  <div class="white-panel"></div>
  <h2 class="headline">Save up to<br>$1000.00<br>or more</h2>
  <p class="subline">with a Balance Transfer Credit Card.</p>
  <a class="cta">Compare the Offers</a>
  <span class="brand-mark"></span>
  <span class="brand-name">CardMatchScout</span>
  <span class="brand-tagline">Find the best credit card for you</span>
</section>

<section class="banner leaderboard" aria-label="728 by 90 banner">
  <svg class="sheen" viewBox="0 0 1077 129" preserveAspectRatio="none" aria-hidden="true">
    <path d="M0 0 L480 0 C360 30 200 60 0 80 Z" fill="var(--blue-light)" opacity=".4"/>
  </svg>
  <div class="white-panel"></div>
  <h2 class="headline">Save up to $1,000</h2>
  <p class="subline">or <em>more</em> in interest with a Balance Transfer Credit Card.</p>
  <a class="cta">Compare the Offers</a>
  <span class="brand-mark"></span>
  <span class="brand-name">CardMatchScout</span>
  <span class="brand-tagline">Find the best credit card for you</span>
</section>

<section class="banner full-banner" aria-label="468 by 60 banner">
  <svg class="sheen" viewBox="0 0 691 86" preserveAspectRatio="none" aria-hidden="true">
    <path d="M0 0 L300 0 C220 20 120 40 0 55 Z" fill="var(--blue-light)" opacity=".4"/>
  </svg>
  <div class="white-panel"></div>
  <h2 class="headline">Save up to $1,000</h2>
  <p class="subline">or <em>more</em> in interest with a Balance Transfer Credit Card.</p>
  <a class="cta">Compare the Offers</a>
  <span class="brand-mark"></span>
  <span class="brand-name">CardMatchScout</span>
  <span class="brand-tagline">Find the best credit card for you</span>
</section>

</body>
</html>
```